Agricultural and Earthmoving business card design

We need a business card design for a new company based in Kilmore, Victoria. We are a versatile company with two specialties, the first is an earthworks side, we do big and small jobs, from soccer fields for councils and football clubs down to house cuts for the public, horse ridding arena's, tennis courts and drainage are also small jobs we have experience in. Not only do we do earthmoving, but we also have a lot of experience in the agricultural side of machinery work, from pasture improvements to a lot of experience in hay contracting. We need a business card that doesn't focus on only one side of our business but blends both skills. We would like a primarily black business card that incorporates our company logo. Our company colours are black red , grey and white.

Industry/Entity Type

House

Contact Information for Business Card

Brantwell Contracting, Neil Brantwell, 2716 Easton Hwy Kilmore Vic 3764, Phone: 03 5924 6308, Mobile: 0427 913 084. Specialising in Earthmoving, synthetic and natural turf, landscaping, drainage. Also specialising in Agricultural improvements and hay contracting.

Requirements
Must have
• A good blend of both earthmoving and agricultural contracting. Company logo.

```html
<!DOCTYPE html>
<html lang="en">
<head>
<meta charset="utf-8">
<title>Brantwell Contracting – Business Card</title>
<link rel="stylesheet" href="https://fonts.googleapis.com/css2?family=Archivo:wght@600;700&family=Josefin+Sans:wght@300;400&display=swap">
<style>
  :root {
    --backdrop: #939598;
    --card-white: #ffffff;
    --brand-red: #ed2024;
    --brand-dark-red: #a8161c;
    --ink-black: #000000;
    --ink-dark: #2b2b2b;
    --card-radius: 32px;
  }
  * { box-sizing: border-box; margin: 0; padding: 0; }
  html, body {
    width: 1200px; height: 1000px; overflow: hidden;
    background: var(--backdrop);
  }
  .canvas { position: relative; width: 1200px; height: 1000px; }

  .card {
    position: absolute;
    width: 640px;
    border-radius: var(--card-radius);
    background: var(--card-white);
    overflow: hidden;
    box-shadow: 0 10px 24px rgba(0,0,0,0.25);
  }

  /* Front */
  .card-front { left: 120px; top: 60px; height: 410px; }
  .brand-lockup {
    position: absolute; left: 0; right: 0; top: 228px;
    display: flex; align-items: center; justify-content: center; gap: 16px;
  }
  .brand-square {
    width: 30px; height: 30px; background: var(--brand-red); flex: none;
  }
  .brand-name {
    font-family: "Archivo", sans-serif; font-weight: 700;
    font-size: 30px; color: var(--brand-dark-red);
    letter-spacing: 1.5px; text-transform: uppercase; white-space: nowrap;
  }
  .tagline-band {
    position: absolute; left: 0; right: 0; top: 318px; height: 52px;
    background: var(--ink-black);
    display: flex; align-items: center; justify-content: center;
  }
  .tagline {
    font-family: "Archivo", sans-serif; font-weight: 600;
    font-size: 19px; color: var(--brand-red); letter-spacing: 0.5px;
    text-transform: uppercase; white-space: nowrap;
  }

  /* Back */
  .card-back { left: 500px; top: 520px; height: 420px; }
  .back-wave { position: absolute; inset: 0; }
  .back-lockup {
    position: absolute; right: 34px; top: 114px;
    display: flex; align-items: center; gap: 10px;
  }
  .back-lockup .brand-square { width: 22px; height: 22px; }
  .back-lockup .brand-name { font-size: 21px; letter-spacing: 1px; }

  .holder {
    position: absolute; left: 46px; top: 250px;
    width: 300px; padding-bottom: 4px;
    border-bottom: 3px solid var(--ink-black);
    font-family: "Josefin Sans", sans-serif; font-weight: 300;
    font-size: 20px; color: var(--ink-dark); letter-spacing: 1px;
    text-transform: uppercase;
  }
  .contact-list {
    position: absolute; left: 46px; top: 300px;
    list-style: none;
    font-family: "Josefin Sans", sans-serif; font-weight: 300;
    color: var(--ink-dark);
  }
  .contact-list li {
    display: flex; align-items: center; gap: 8px;
    height: 23px; font-size: 17px; white-space: nowrap;
  }
  .contact-list li.small { font-size: 15px; }
  .contact-icon {
    width: 18px; height: 18px; flex: none;
    background: var(--ink-dark); border-radius: 2px;
  }
  .address {
    position: absolute; left: 420px; top: 304px;
    font-family: "Josefin Sans", sans-serif; font-weight: 300;
    font-size: 16px; line-height: 23px; color: var(--ink-dark);
  }
</style>
</head>
<body>
<main class="canvas">

  <section class="card card-front" aria-label="Business card front">
    <div class="brand-lockup">
      <span class="brand-square"></span>
      <span class="brand-name">Brantwell Contracting</span>
    </div>
    <div class="tagline-band">
      <p class="tagline">Earthmoving and Agricultural Contracting</p>
    </div>
  </section>

  <section class="card card-back" aria-label="Business card back">
    <svg class="back-wave" width="640" height="420" viewBox="0 0 640 420" aria-hidden="true">
      <path d="M0 100 C 180 130, 380 215, 640 232 L640 420 L0 420 Z" fill="var(--brand-red)"/>
    </svg>

    <div class="back-lockup">
      <span class="brand-square"></span>
      <span class="brand-name">Brantwell Contracting</span>
    </div>

    <p class="holder">Neil Brantwell</p>

    <ul class="contact-list">
      <li>
        <svg class="contact-icon" viewBox="0 0 18 18" aria-hidden="true"><path d="M5 3 L7.5 6 L6 7.8 C7 10 8.2 11.2 10.2 12 L12 10.5 L15 13 L13.5 15 C8 15 3 10 3 4.5 Z" fill="#ed2024"/></svg>
        03 5924 6308
      </li>
      <li>
        <svg class="contact-icon" viewBox="0 0 18 18" aria-hidden="true"><rect x="6" y="3" width="6" height="12" rx="1" fill="#ed2024"/></svg>
        0427 913 084
      </li>
      <li class="small">
        <svg class="contact-icon" viewBox="0 0 18 18" aria-hidden="true"><rect x="3" y="5" width="12" height="8" fill="#ed2024"/><path d="M3 5 L9 10 L15 5" stroke="#2b2b2b" fill="none"/></svg>
        neil@brantwellcontracting.com.au
      </li>
      <li class="small">
        <svg class="contact-icon" viewBox="0 0 18 18" aria-hidden="true"><circle cx="9" cy="9" r="5.5" fill="none" stroke="#ed2024" stroke-width="1.2"/><path d="M3.5 9 H14.5 M9 3.5 V14.5" stroke="#ed2024" stroke-width="1"/></svg>
        www.brantwellcontracting.com.au
      </li>
    </ul>

    <p class="address">2716 Easton Hwy,<br>Ashby Vic 3519</p>
  </section>

</main>
</body>
</html>
```